Fence Contractor Website Design

We are working with Yardline Works. They are a local fencing and automatic gate installer and in need of a new website design.
Some sites to use for inspiration:
https://pinevalebarrier.example
https://marwickrails.example
https://www.tellurpostsandboards.example
https://www.grovanpaneling.example
Thank you for taking the time to consider designing a website for us. We are web developers based in Stockton, CA, USA. Most of our projects go through the same process. Understanding this process may help you win a project with us. We custom-code all of our websites in-house. We don’t have any requirements as to what tools you use for your design, but we prefer Figma files. For any design that we label as four-stars, we send it to the client for review. The client picks the final design they want us to use. Once we complete this process, we will continue to show additional clients all the four-star sites and purchase them later. Your designs will have multiple chances to sell. For better chances of success, we ask that you follow these guidelines.
IMAGES:
If you use any images or icons in the design, we ask that you have a link to the asset so we can purchase the image/icon. Most of the designs we submit do not have the customer’s images on them unless they have some great images. Be creative; show us the feeling you are trying to portray with your image choices. Use any royalty-free site you choose. We subscribe to Stockvane and mainly use their images, but we can purchase images outside of Stockvane.
PLEASE NOTE: we will not submit designs to clients with watermarks on the images.
FONTS:
We ask that you identify the fonts used in the design. This can be done in a message if you want. We typically use Google Fonts and Stockvane Fonts.
CONTENT:
We're always open to different content and ideas. We often submit designs with stock images so the client can see our vision. We typically take pictures after the website launch to use their images with our vision. Lorem Ipsum is fine for paragraphs, but we ask that you write the headers in correct English. We want to be able to show the vision and identify the sections of the website.
INSPIRATION:
We typically add a couple of links in the brief of websites we like to help you get started in your design.
REVISIONS:
We do not often ask for revisions of the designs unless we see something in the design that may not appeal to the client. If there are slight changes that we want to make, we do that in the development process.
FEEDBACK:
We rarely give feedback on designs during the design process. We are working on many website projects and do not have the time to provide feedback. We usually respond if your request is well thought out and asks specific questions, but a note asking “feedback, please” usually goes unanswered.
Number of Pages Required
1 page
Look and feel
Each slider illustrates characteristics of the customer's brand and the style your logo design should communicate.

```html
<!DOCTYPE html>
<html lang="en">
<head>
<meta charset="utf-8">
<title>Yardline Works — Fencing &amp; Gates</title>
<link rel="stylesheet" href="https://fonts.googleapis.com/css2?family=Orbitron:wght@700;900&family=Michroma&family=Montserrat:wght@400;500;600;700&display=swap">
<style>
:root{
  --navy:#1b2a4a;
  --navy-deep:#14203b;
  --red:#ee1c1c;
  --white:#ffffff;
  --ink:#2b2b2b;
  --muted:#5b6270;
  --blush:#fdf1f0;
  --line:#d9dce2;
}
*{box-sizing:border-box;margin:0;padding:0}
html,body{width:1200px;height:4242px;overflow:hidden}
body{position:relative;background:var(--white);font-family:"Montserrat",sans-serif;color:var(--ink)}
.abs{position:absolute}
.display{font-family:"Orbitron",sans-serif;font-weight:900;letter-spacing:1px;text-transform:uppercase}
.wide{font-family:"Michroma",sans-serif;text-transform:uppercase}
.btn{position:absolute;display:flex;align-items:center;justify-content:center;background:var(--red);color:var(--white);
  font-family:"Orbitron",sans-serif;font-weight:900;font-size:15px;letter-spacing:1px;text-transform:uppercase;
  clip-path:polygon(7% 0,93% 0,100% 50%,93% 100%,7% 100%,0 50%)}
.eyebrow{position:absolute;display:flex;align-items:center;gap:14px;font-weight:600;font-size:19px;letter-spacing:1px;color:var(--muted);text-transform:uppercase}
.eyebrow::before,.eyebrow::after{content:"";width:30px;height:2px;background:currentColor}
.eyebrow.left::before{display:none}

/* header */
.topbar{top:0;left:0;width:1200px;height:95px;background:var(--white)}
.estimate-tag{top:22px;left:505px;width:228px;height:50px;background:var(--navy);color:var(--red);font-size:12px;
  display:flex;align-items:center;justify-content:center;clip-path:polygon(8% 0,92% 0,100% 50%,92% 100%,8% 100%,0 50%)}
.call-box{top:0;left:790px;width:410px;height:95px;background:var(--red);color:var(--white)}
.call-icon{position:absolute;left:-20px;top:10px;width:66px;height:72px;background:var(--navy);clip-path:polygon(50% 0,100% 25%,100% 75%,50% 100%,0 75%,0 25%);display:flex;align-items:center;justify-content:center}
.call-box .label{position:absolute;left:82px;top:22px;font-weight:700;font-size:14px}
.call-box .num{position:absolute;left:82px;top:46px;font-family:"Orbitron",sans-serif;font-weight:900;font-size:23px;letter-spacing:2px}
.navbar{top:95px;left:0;width:1200px;height:75px;background:var(--navy)}
.nav{position:absolute;left:405px;top:0;height:75px;display:flex;align-items:center}
.nav a{color:var(--white);text-decoration:none;font-size:13px;padding:0 22px;height:75px;display:flex;align-items:center;position:relative}
.nav a + a::before{content:"";position:absolute;left:-3px;top:35px;width:6px;height:6px;border-radius:50%;background:var(--red)}
.nav a.active{background:var(--red)}
.brand-plate{top:0;left:92px;width:263px;height:245px;background:var(--white);clip-path:polygon(0 0,100% 0,100% 72%,50% 100%,0 72%);z-index:3;
  display:flex;flex-direction:column;align-items:center;justify-content:center;gap:10px;padding-bottom:40px}
.brand-name{font-weight:700;font-size:27px;color:var(--navy);text-align:center;line-height:1.05}
.brand-square{width:22px;height:22px;background:var(--red)}

/* hero */
.hero{top:170px;left:0;width:1200px;height:600px;clip-path:polygon(0 0,100% 0,100% 78%,50% 100%,0 78%);
  background:linear-gradient(90deg,rgba(20,32,59,.75) 0%,rgba(20,32,59,.25) 50%,rgba(20,32,59,0) 70%),
  linear-gradient(180deg,#7ea6c9 0%,#b8cfe0 30%,#dfe6e9 46%,#4f7a3a 60%,#2f5a24 100%)}
.hero h1{position:absolute;left:110px;top:130px;width:560px;color:var(--white);font-size:37px;line-height:52px}
.hero p{position:absolute;left:110px;top:285px;width:470px;color:var(--white);font-weight:600;font-size:15px;line-height:29px}
.hero-lines{top:685px;left:0}
.hero-badge{top:718px;left:560px;width:80px;height:80px;border-radius:50%;background:var(--white);border:3px solid var(--navy)}

/* about */
.about-mark{top:850px;left:18px;width:510px;height:430px;display:flex;flex-direction:column;align-items:center;justify-content:center;gap:20px}
.about-mark .brand-name{font-size:58px}
.about h2{position:absolute;left:598px;top:850px;font-size:37px;color:var(--navy)}
.about h2 span,.red{color:var(--red)}
.about-copy{position:absolute;left:598px;top:935px;width:490px;font-size:15px;line-height:27.5px;color:var(--ink);text-align:justify}
.about-copy p+p{margin-top:27px}

/* services */
.fence-band{left:0;width:1200px;height:170px;background:linear-gradient(180deg,#eef0f4,#dcdfe6)}
.services{top:1400px;left:0;width:1200px;height:1072px;background:linear-gradient(180deg,var(--navy) 0%,#1f2f52 55%,var(--navy-deep) 100%);
  clip-path:polygon(0 12%,50% 0,100% 12%,100% 100%,0 100%)}
.services-title{top:1515px;left:0;width:1200px;text-align:center;color:var(--white);font-size:37px}
.service{position:absolute;top:1630px;width:190px;text-align:center;color:var(--white);font-size:17px;line-height:25px}
.hex{width:106px;height:120px;margin:0 auto 12px;background:var(--navy);border:0;clip-path:polygon(50% 0,100% 25%,100% 75%,50% 100%,0 75%,0 25%);
  display:flex;align-items:center;justify-content:center;position:relative}
.hex-outline{position:absolute;inset:0;background:#3b4a6c;clip-path:inherit}
.hex-inner{position:absolute;inset:2px;background:#223256;clip-path:polygon(50% 0,100% 25%,100% 75%,50% 100%,0 75%,0 25%);display:flex;align-items:center;justify-content:center}
.service.active .hex-outline,.service.active .hex-inner{background:var(--red)}
.commercial h3{position:absolute;left:110px;top:1902px;color:var(--white);font-size:36px;line-height:46px}
.commercial p{position:absolute;left:110px;top:2005px;width:460px;color:var(--white);font-size:15px;line-height:31px}
.perks{position:absolute;left:110px;top:2110px;list-style:none;color:var(--white);font-weight:500;font-size:19px}
.perks li{height:47px;display:flex;gap:8px}
.perks li::before{content:"★";color:var(--red)}
.hex-photo{top:1878px;left:637px;width:451px;height:520px;clip-path:polygon(50% 0,100% 25%,100% 75%,50% 100%,0 75%,0 25%);
  background:linear-gradient(180deg,#d9e4ee 0%,#c3ccd3 35%,#8d949b 60%,#9a7f6e 100%)}

/* testimonials */
.section-title{left:0;width:1200px;text-align:center;font-size:37px;color:var(--navy)}
.card{position:absolute;width:311px;background:var(--white);border:1px solid var(--line);box-shadow:0 4px 16px rgba(20,32,59,.08);padding:18px 16px;font-size:14px;line-height:27.5px;color:var(--ink)}
.stars{color:#f2a900;font-size:17px;letter-spacing:1px;margin-bottom:4px}
.author{display:flex;align-items:center;gap:12px;margin-top:16px}
.avatar{width:62px;height:62px;border-radius:50%;background:linear-gradient(135deg,#c9d3de,#8a97a8)}
.author b{display:block;font-family:"Orbitron",sans-serif;font-weight:900;font-size:15px;letter-spacing:1px;color:var(--navy);text-transform:uppercase;line-height:20px}
.author small{font-size:13px;font-weight:600;color:#8a8f98}

/* contact */
.contact{top:3138px;left:0;width:1200px;height:620px;background:var(--blush)}
.contact-lead{left:110px;top:3325px;font-weight:700;font-size:20px;color:var(--navy)}
.contact-copy{left:110px;top:3366px;width:360px;font-size:15px;line-height:31px;color:var(--muted)}
.info{position:absolute;left:110px;display:flex;gap:15px;align-items:center}
.info .dot{width:64px;height:64px;border-radius:50%;background:var(--red);display:flex;align-items:center;justify-content:center}
.info small{display:block;font-weight:700;font-size:17px;color:var(--muted);letter-spacing:1px;text-transform:uppercase}
.info b{font-size:17px;color:var(--ink)}
.field{position:absolute;height:48px;background:var(--white);box-shadow:0 3px 10px rgba(0,0,0,.06);font-weight:600;font-size:14px;color:#444;padding:0 17px;display:flex;align-items:center}

/* footer */
.footer{top:3800px;left:0;width:1200px;height:442px;background:linear-gradient(180deg,#1f2f56,var(--navy-deep));clip-path:polygon(0 18%,50% 0,100% 18%,100% 100%,0 100%)}
.footer-mark{top:3830px;left:400px;width:400px;height:220px;display:flex;flex-direction:column;align-items:center;justify-content:center;gap:14px}
.footer-mark .brand-name{color:var(--white);font-size:40px}
.footer-nav{top:4100px;left:0;width:1200px;display:flex;justify-content:center;gap:75px;color:var(--white);font-size:17px}
.copyright{top:4168px;left:0;width:1200px;text-align:center;color:var(--white);font-size:15px}
</style>
</head>
<body>

<!-- header -->
<div class="abs topbar"></div>
<div class="abs estimate-tag wide">Free Estimates</div>
<div class="abs call-box">
  <div class="call-icon">
    <svg width="30" height="30" viewBox="0 0 24 24" fill="#ee1c1c"><path d="M6.6 10.8a15.1 15.1 0 0 0 6.6 6.6l2.2-2.2c.3-.3.7-.4 1-.2 1.1.4 2.3.6 3.6.6.6 0 1 .4 1 1V20c0 .6-.4 1-1 1A17 17 0 0 1 3 4c0-.6.4-1 1-1h3.5c.6 0 1 .4 1 1 0 1.3.2 2.5.6 3.6.1.3 0 .7-.2 1z"/></svg>
  </div>
  <div class="label">CALL US</div>
  <div class="num">+1 888 888 8888</div>
</div>
<div class="abs navbar">
  <nav class="nav wide">
    <a class="active">Home</a><a>About</a><a>Services</a><a>Testimonial</a><a>Contact Us</a>
  </nav>
</div>
<div class="abs brand-plate">
  <div class="brand-name">Yardline<br>Works</div>
  <div class="brand-square"></div>
</div>

<!-- hero -->
<section class="abs hero" role="img" aria-label="Photo of a white vinyl privacy fence running along a green lawn with trees">
  <h1 class="display">Secure. Stylish. Reliable Fencing Solutions.</h1>
  <p>Yardline Works has been providing high-quality fencing and automatic gate solutions for residential and commercial clients for years.</p>
</section>
<a class="btn" style="left:110px;top:553px;width:287px;height:55px">Get a Free Quote</a>
<svg class="abs hero-lines" width="1200" height="110" viewBox="0 0 1200 110">
  <polygon points="250,7 600,95 950,7 600,80" fill="#ee1c1c"/>
  <polygon points="300,2 600,78 900,2 600,66" fill="#1b2a4a" opacity=".0"/>
</svg>
<div class="abs hero-badge"></div>

<!-- about -->
<section class="about">
  <div class="abs about-mark">
    <div class="brand-name">Yardline Works</div>
    <div class="brand-square" style="width:60px;height:60px"></div>
  </div>
  <h2 class="display">About <span>Yardline</span></h2>
  <div class="eyebrow left" style="left:598px;top:900px">Fencing &amp; Gates</div>
  <div class="about-copy">
    <p>Yardline Works has been providing high-quality fencing and automatic gate solutions for residential and commercial clients for years. Our team is dedicated to delivering durable, safe, and visually appealing fences tailored to your needs. From design and installation to maintenance, we ensure every project is completed with precision and care.</p>
    <p>Our mission is simple: to deliver high-quality fences and gates that meet your unique needs while providing outstanding customer service from start to finish.</p>
  </div>
  <a class="btn" style="left:600px;top:1222px;width:192px;height:54px">Read More</a>
</section>

<!-- services -->
<div class="abs fence-band" style="top:1350px" role="img" aria-label="Row of white picket fence boards with small star accents"></div>
<div class="abs services"></div>
<svg class="abs" style="top:1388px;left:0" width="1200" height="80" viewBox="0 0 1200 80">
  <polygon points="330,66 600,2 870,66 600,16" fill="#ee1c1c"/>
</svg>
<h2 class="abs services-title display">Our Services</h2>
<div class="eyebrow" style="left:497px;top:1573px;color:#b9c0cc">We Offer</div>

<div class="service" style="left:118px">
  <div class="hex"><div class="hex-outline"></div><div class="hex-inner">
    <svg width="52" height="44" viewBox="0 0 52 44" fill="none" stroke="#7f93bd" stroke-width="3"><path d="M6 22 26 6l20 16M12 18v22h28V18"/><path d="M20 40V28h12v12"/></svg>
  </div></div>Residential<br>Fencing</div>
<div class="service active" style="left:310px">
  <div class="hex"><div class="hex-outline"></div><div class="hex-inner">
    <svg width="56" height="46" viewBox="0 0 56 46" fill="#fff"><rect x="4" y="8" width="6" height="36"/><rect x="14" y="8" width="6" height="36"/><rect x="24" y="8" width="6" height="36"/><rect x="34" y="8" width="6" height="36"/><rect x="44" y="8" width="6" height="36"/><rect x="0" y="16" width="56" height="5"/><rect x="0" y="31" width="56" height="5"/></svg>
  </div></div>Commercial<br>Fencing</div>
<div class="service" style="left:503px">
  <div class="hex"><div class="hex-outline"></div><div class="hex-inner">
    <svg width="56" height="46" viewBox="0 0 56 46" fill="none" stroke="#7f93bd" stroke-width="3"><path d="M4 44V8M52 44V8M4 14q24-10 48 0M4 40h48M16 10v30M28 8v32M40 10v30"/></svg>
  </div></div>Automatic Gate<br>Installation</div>
<div class="service" style="left:695px">
  <div class="hex"><div class="hex-outline"></div><div class="hex-inner">
    <svg width="56" height="46" viewBox="0 0 56 46" fill="none" stroke="#7f93bd" stroke-width="3"><path d="M8 44V16M18 44V12M28 44V16M38 44V12M2 24h44M2 36h44M34 4l16 16"/></svg>
  </div></div>Fence Repairs<br>&amp; Maintenance</div>
<div class="service" style="left:892px">
  <div class="hex"><div class="hex-outline"></div><div class="hex-inner">
    <svg width="56" height="46" viewBox="0 0 56 46" fill="none" stroke="#7f93bd" stroke-width="3"><path d="M8 42V10M20 42V10M32 42V10M44 42V10M2 20h52M2 32h52"/></svg>
  </div></div>Custom Fence<br>Design</div>

<section class="commercial">
  <h3 class="display">Commercial<br>Fencing</h3>
  <p>Our commercial fences are designed to offer maximum security, durability, and functionality while meeting regulatory requirements.</p>
  <ul class="perks">
    <li>Enhanced Security</li>
    <li>Durable Materials, Custom Designs</li>
    <li>Automatic Gate Integration</li>
    <li>Compliance &amp; Safety and&nbsp; Low Maintenance</li>
  </ul>
  <a class="btn" style="left:110px;top:2306px;width:202px;height:55px">Read More</a>
  <div class="abs hex-photo" role="img" aria-label="Photo of a steel commercial sliding gate in front of an industrial building"></div>
</section>

<!-- testimonials -->
<h2 class="abs section-title display" style="top:2540px">What Our <span class="red">Customer Says</span></h2>
<div class="eyebrow" style="left:475px;top:2595px">Testimonials</div>

<div class="card" style="left:104px;top:2665px">
  <div class="stars">★★★★★</div>
  Yardline Works transformed our backyard with a beautiful and sturdy fence. The installation was quick, and the team was professional and friendly throughout. Highly recommend! The team was professional, efficient, and friendly — couldn't be happier!
  <div class="author"><div class="avatar"></div><div><b>Marcus Reed</b><small>Facility Manager</small></div></div>
</div>
<div class="card" style="left:445px;top:2708px">
  <div class="stars">★★★★★</div>
  We've used Yardline Works multiple times for fencing repairs and upgrades. Their team is reliable, knowledgeable, and always goes the extra mile to ensure satisfaction. They delivered on time with excellent workmanship and attention to detail.
  <div class="author"><div class="avatar"></div><div><b>Helena</b><small>Property Owner</small></div></div>
</div>
<div class="card" style="left:785px;top:2665px">
  <div class="stars">★★★★★</div>
  We needed a secure fence and automatic gate for our warehouse. Yardline Works delivered exactly what we needed — on time, on budget, and with excellent workmanship. We've used them multiple times for fencing repairs and upgrades.
  <div class="author"><div class="avatar"></div><div><b>Owen Pratt</b><small>Homeowner</small></div></div>
</div>

<!-- contact -->
<section class="abs contact"></section>
<h2 class="abs section-title display" style="top:3205px">Get In <span class="red">Touch With Us</span></h2>
<div class="eyebrow" style="left:487px;top:3260px">Contact Us</div>
<div class="abs contact-lead">Need our service? Please call us:</div>
<p class="abs contact-copy">From residential to commercial, our expert team delivers fencing and gate solutions from design to installation with care.</p>
<div class="info" style="top:3482px">
  <div class="dot"><svg width="26" height="26" viewBox="0 0 24 24" fill="#fff"><path d="M6.6 10.8a15.1 15.1 0 0 0 6.6 6.6l2.2-2.2c.3-.3.7-.4 1-.2 1.1.4 2.3.6 3.6.6.6 0 1 .4 1 1V20c0 .6-.4 1-1 1A17 17 0 0 1 3 4c0-.6.4-1 1-1h3.5c.6 0 1 .4 1 1 0 1.3.2 2.5.6 3.6.1.3 0 .7-.2 1z"/></svg></div>
  <div><small>Phone Number</small><b>+1 888 888 8888</b></div>
</div>
<div class="info" style="top:3575px">
  <div class="dot"><svg width="26" height="22" viewBox="0 0 26 20" fill="#fff"><path d="M1 0h24c.6 0 1 .4 1 1v.6L13 10 0 1.6V1c0-.6.4-1 1-1zM0 4l13 8.4L26 4v15c0 .6-.4 1-1 1H1c-.6 0-1-.4-1-1z"/></svg></div>
  <div><small>Email Address</small><b>info@yardlineworks.example</b></div>
</div>
<div class="field" style="left:505px;top:3333px;width:283px">First Name</div>
<div class="field" style="left:800px;top:3333px;width:283px">Your Email</div>
<div class="field" style="left:505px;top:3395px;width:283px">Your Phone</div>
<div class="field" style="left:800px;top:3395px;width:283px;justify-content:space-between">Services<span style="font-size:10px">▼</span></div>
<div class="field" style="left:505px;top:3458px;width:578px;height:112px;align-items:flex-start;padding-top:16px">Message</div>
<a class="btn" style="left:507px;top:3630px;width:192px;height:55px">Submit</a>

<!-- footer -->
<div class="abs fence-band" style="top:3730px;height:110px" role="img" aria-label="Row of white picket fence boards with small star accents"></div>
<div class="abs footer" role="img" aria-label="Dusk photo of a dark wooden fence and house, tinted navy"></div>
<svg class="abs" style="top:3788px;left:0" width="1200" height="70" viewBox="0 0 1200 70">
  <polygon points="330,60 600,2 870,60 600,14" fill="#ee1c1c"/>
</svg>
<div class="abs footer-mark">
  <div class="brand-name">Yardline Works</div>
  <div class="brand-square" style="width:36px;height:36px"></div>
</div>
<nav class="abs footer-nav wide"><span>Home</span><span>About</span><span>Services</span><span>Testimonial</span><span>Contact Us</span></nav>
<div class="abs copyright wide">Copyrights©2025 Yardline Works. All Rights Reserved</div>

</body>
</html>
```